Picture Ads

We need some banner ads for our home business opportunity, we are evolving from text to picture ads. I have added some examples of what other distributors are using. We are looking for something really eye catching with some good key words and nice bright colours and to include our photo (attached)
Key words to include:
Booming online business
Personal Development and Leadership Industry
Earn an executive income from home
Simple 3 step system
Make up to $5,000 per sale
Not MLM
The size needs to be: 1000 x 35 pixels
13.9 x 4.75 Inches
35.3 x 11.1 cm
I think different platforms accept different sizes, not too familiar with it yet, any guidance welcome. I've clicked project for 2 days if that is to prioritise the order?
Many thanks,
Maren

Industry/Entity Type

Business

```html
<!DOCTYPE html>
<html lang="en">
<head>
<meta charset="utf-8">
<title>Booming Online Business Banner</title>
<link href="https://fonts.googleapis.com/css2?family=Oswald:wght@500;600&family=Courgette&family=Montserrat:wght@500&display=swap" rel="stylesheet">
<style>
  :root {
    --navy-deep: #071233;
    --navy: #0b1f5c;
    --blue-glow: #1d4fc4;
    --white: #ffffff;
    --yellow: #f6f000;
    --cyan: #38cdf2;
    --frame: #f7f7f7;
    --photo-dark: #2b1c18;
    --photo-warm: #8a5a40;
    --photo-light: #c9a27c;
  }
  html, body {
    margin: 0;
    padding: 0;
    width: 1200px;
    height: 378px;
    overflow: hidden;
    background: var(--navy-deep);
  }
  .banner {
    position: relative;
    width: 1200px;
    height: 378px;
    overflow: hidden;
    background:
      radial-gradient(ellipse 70% 22% at 45% 58%, rgba(60,120,240,0.55), rgba(29,79,196,0) 70%),
      linear-gradient(180deg, var(--navy-deep) 0%, var(--navy) 38%, var(--blue-glow) 52%, var(--navy) 68%, var(--navy-deep) 100%);
  }
  .banner__streaks {
    position: absolute;
    inset: 0;
  }
  .headline {
    position: absolute;
    left: 46px;
    top: 2px;
    margin: 0;
    font-family: "Oswald", sans-serif;
    font-weight: 500;
    font-size: 88px;
    line-height: 1;
    color: var(--white);
    white-space: nowrap;
    transform: scaleX(0.83);
    transform-origin: left top;
  }
  .tagline {
    position: absolute;
    left: 106px;
    top: 96px;
    margin: 0;
    font-family: "Courgette", cursive;
    font-size: 30px;
    color: var(--white);
    white-space: nowrap;
  }
  .offer {
    position: absolute;
    left: 58px;
    top: 166px;
    margin: 0;
    font-family: "Oswald", sans-serif;
    font-weight: 600;
    font-size: 64px;
    line-height: 1;
    color: var(--yellow);
    white-space: nowrap;
    transform: scaleX(0.78);
    transform-origin: left top;
  }
  .benefits {
    position: absolute;
    left: 62px;
    top: 248px;
    margin: 0;
    padding: 0;
    list-style: none;
    font-family: "Montserrat", sans-serif;
    font-weight: 500;
    font-size: 28px;
    color: var(--cyan);
  }
  .benefits li {
    display: flex;
    align-items: center;
    height: 36px;
  }
  .benefits svg {
    width: 20px;
    height: 20px;
    margin-right: 14px;
    fill: var(--cyan);
  }
  .portrait {
    position: absolute;
    left: 786px;
    top: -142px;
    width: 420px;
    height: 460px;
    background: var(--frame);
    transform: rotate(15deg);
    transform-origin: left bottom;
    box-shadow: 0 4px 14px rgba(0,0,0,0.45);
  }
  .portrait__photo {
    position: absolute;
    inset: 14px;
    background:
      radial-gradient(ellipse 40% 40% at 30% 65%, var(--photo-warm), rgba(138,90,64,0) 70%),
      radial-gradient(ellipse 35% 45% at 70% 62%, var(--photo-light), rgba(201,162,124,0) 70%),
      linear-gradient(160deg, var(--photo-dark), #4a3228 60%, var(--photo-dark));
  }
</style>
</head>
<body>
  <div class="banner">
    <svg class="banner__streaks" width="1200" height="378" viewBox="0 0 1200 378" aria-hidden="true">
      <path d="M0 190 C300 160 700 200 1200 170" stroke="rgba(120,180,255,0.25)" stroke-width="3" fill="none"/>
      <path d="M0 230 C350 250 750 215 1200 240" stroke="rgba(120,180,255,0.18)" stroke-width="2" fill="none"/>
      <path d="M0 150 L1200 140" stroke="rgba(0,0,0,0.25)" stroke-width="1" fill="none"/>
    </svg>

    <h1 class="headline">BOOMING ONLINE BUSINESS</h1>
    <p class="tagline">Personal Development and Leadership Industry</p>
    <p class="offer">MAKE UP TO $5,000 PER SALE</p>

    <ul class="benefits">
      <li><svg viewBox="0 0 24 24"><path d="M12 1.5l3.1 6.9 7.4.7-5.6 5 1.7 7.4L12 17.6l-6.6 3.9 1.7-7.4-5.6-5 7.4-.7z"/></svg>Simple 3 step system</li>
      <li><svg viewBox="0 0 24 24"><path d="M12 1.5l3.1 6.9 7.4.7-5.6 5 1.7 7.4L12 17.6l-6.6 3.9 1.7-7.4-5.6-5 7.4-.7z"/></svg>Make up to $5,000 per sale</li>
      <li><svg viewBox="0 0 24 24"><path d="M12 1.5l3.1 6.9 7.4.7-5.6 5 1.7 7.4L12 17.6l-6.6 3.9 1.7-7.4-5.6-5 7.4-.7z"/></svg>Not MLM</li>
    </ul>

    <div class="portrait">
      <div class="portrait__photo" role="img" aria-label="Photo of the two business owners smiling together"></div>
    </div>
  </div>
</body>
</html>
```